Lumen Business Cards

We need a new look business cvard to refelect our new look website www.lumenplan.com.au
We’re Lumen, a team of town planning and traffic and transport engineering specialists located in Melbourne.

Lumen is a company that is structured, articulate, dynamic, progressive, accurate and adaptable.
Our key messages are:
1. We make your life easier by doing what we do best
2. We tell you what you need to know not what you want to hear
3. Polished and professional but not afraid to show some personality

we would like a bold new look that is polished and professional but not afraid to show a bit of personality

Target Market(s)

Lumen’s diverse client base consists of architecture practices, builders, developers, local government and the legal fraternity.

Industry/Entity Type

Town

Requirements
Must have
• must use our logo and have the following information

Joel Petrakis
Director

Lumen Advisory Pty Ltd
Hillgate first floor
Cotter Street
Kewdale VIC 3187 Australia
+61 03 9581 6724
mail@lumenplan.com.au
www.lumenplan.com.au
Nice to have
• We would like to see the logo used or the colours of the logo used.

```html
<!DOCTYPE html>
<html lang="en">
<head>
<meta charset="utf-8">
<title>Lumen Business Cards</title>
<link rel="stylesheet" href="https://fonts.googleapis.com/css2?family=Open+Sans:wght@300;400;600&display=swap">
<style>
  :root {
    --backdrop: #2b2d31;
    --card-light: #fafafa;
    --card-shade: #e6e7e8;
    --band-dark: #4a4b4f;
    --stripe-mid: #8e9094;
    --stripe-soft: #c4c6c9;
    --stripe-pale: #dcdee0;
    --brand-teal: #6fb8c8;
    --brand-slate: #7f98a6;
    --accent-pink: #e4148c;
    --text-dark: #3d3e42;
    --text-light: #ffffff;
  }
  html, body {
    margin: 0;
    width: 1200px;
    height: 1000px;
    overflow: hidden;
    background: var(--backdrop);
    font-family: "Open Sans", sans-serif;
  }
  .card {
    position: absolute;
    left: 200px;
    width: 800px;
    height: 457px;
    overflow: hidden;
    background: linear-gradient(160deg, var(--card-light) 0%, var(--card-shade) 100%);
    box-shadow: 0 10px 30px rgba(0,0,0,.45);
  }
  .card--front { top: 30px; }
  .card--back { top: 513px; }
  .card__bands {
    position: absolute;
    inset: 0;
  }
  .brand {
    position: absolute;
    display: flex;
    align-items: center;
    gap: 14px;
    color: var(--brand-slate);
    font-weight: 300;
    line-height: 1;
  }
  .brand__mark {
    background: var(--brand-teal);
  }
  .card--front .brand { left: 300px; top: 120px; font-size: 76px; }
  .card--front .brand__mark { width: 46px; height: 46px; }
  .card--back .brand { left: 60px; top: 170px; font-size: 64px; }
  .card--back .brand__mark { width: 38px; height: 38px; }
  .tagline {
    position: absolute;
    left: 280px;
    top: 268px;
    margin: 0;
    color: var(--text-light);
    font-size: 19px;
    font-weight: 400;
    letter-spacing: .2px;
  }
  .person {
    position: absolute;
    right: 50px;
    top: 40px;
    text-align: left;
  }
  .person__name {
    margin: 0;
    color: var(--accent-pink);
    font-size: 20px;
    font-weight: 400;
    border-bottom: 1.5px solid var(--text-dark);
    padding: 0 4px 2px 6px;
  }
  .person__role {
    margin: 2px 0 0 6px;
    color: var(--stripe-mid);
    font-size: 12px;
  }
  .contact {
    position: absolute;
    left: 0;
    top: 262px;
    margin: 0;
    padding: 0;
    list-style: none;
    font-size: 17px;
  }
  .contact li {
    height: 45px;
    line-height: 45px;
    white-space: nowrap;
  }
  .contact__address { padding-left: 56px; color: var(--text-light); }
  .contact__phone { padding-left: 76px; color: var(--text-light); }
  .contact__email { padding-left: 96px; color: var(--text-dark); }
  .contact__web { padding-left: 116px; color: var(--text-dark); }
</style>
</head>
<body>

<section class="card card--front" aria-label="Card front">
  <svg class="card__bands" viewBox="0 0 800 457" aria-hidden="true">
    <polygon points="560,180 800,180 800,222 520,222" fill="var(--stripe-soft)"/>
    <polygon points="520,222 800,222 800,262 480,262" fill="var(--stripe-mid)"/>
    <polygon points="260,262 800,262 800,302 220,302" fill="var(--band-dark)"/>
    <polygon points="220,302 800,302 800,340 500,340" fill="var(--stripe-mid)"/>
    <polygon points="0,340 800,340 800,372 0,372" fill="var(--stripe-pale)"/>
    <polygon points="0,386 800,386 800,414 0,414" fill="var(--stripe-pale)"/>
    <polygon points="0,428 800,428 800,457 0,457" fill="var(--stripe-pale)"/>
  </svg>
  <div class="brand"><span class="brand__mark"></span><span class="brand__name">Lumen</span></div>
  <p class="tagline">We make your life easier by doing what we do best</p>
</section>

<section class="card card--back" aria-label="Card back">
  <svg class="card__bands" viewBox="0 0 800 457" aria-hidden="true">
    <polygon points="620,130 800,130 800,175 590,175" fill="var(--stripe-pale)"/>
    <polygon points="590,175 800,175 800,220 560,220" fill="var(--stripe-soft)"/>
    <polygon points="560,220 800,220 800,262 530,262" fill="var(--stripe-pale)"/>
    <polygon points="0,262 660,262 640,307 0,307" fill="var(--band-dark)"/>
    <polygon points="0,307 640,307 620,352 0,352" fill="var(--stripe-mid)"/>
    <polygon points="0,352 620,352 600,397 0,397" fill="var(--stripe-soft)"/>
    <polygon points="0,397 800,397 800,442 0,442" fill="var(--stripe-pale)"/>
  </svg>
  <div class="person">
    <p class="person__name">Joel Petrakis</p>
    <p class="person__role">Director</p>
  </div>
  <div class="brand"><span class="brand__mark"></span><span class="brand__name">Lumen</span></div>
  <ul class="contact">
    <li class="contact__address">a: Lumen Advisory Pty Ltd, Hillgate first floor, Cotter Street</li>
    <li class="contact__phone">t: +61 03 9581 6724 / f:</li>
    <li class="contact__email">e: mail@lumenplan.com.au</li>
    <li class="contact__web">w: www.lumenplan.com.au</li>
  </ul>
</section>

</body>
</html>
```